BrightLane Real Estate Sign

We are in the process of rebranding our business and need a new For Sale \ Sold sign.
We're a prestige real estate agency and therefore require a really stylish sign.
I've uploaded the following files
1. The new company logo
2. "sample sign.jpg" which shows the type of sign we would like. It is a metal sign with a top panel and bottom panel.
3. Our previous sign "previous sign.jpg" if you're interested in seeing it.
The sign must be black with white text.
Our thoughts are that the top panel (refer to sample sign) would contain the text "For Sale" or "Sold". These would be two separate panels which are interchangeable and could be screwed in place.
The bottom panel would not contain any photos like the sample. However, it may contain our logo and my contact details etc.
The sign is 900mm wide x 1200mm high.
My details are:
Name: Desmond Harlow
Web: www.blrealestate.com.au
Email: sales@blrealestate.com.au
Phone: 0491 836 205

```html
<!DOCTYPE html>
<html lang="en">
<head>
<meta charset="utf-8">
<title>BrightLane Real Estate – For Sale Sign</title>
<link rel="stylesheet" href="https://fonts.googleapis.com/css2?family=Open+Sans:wght@400;600;700&display=swap">
<style>
  :root {
    --header-black: #262626;
    --panel-charcoal: #333232;
    --sign-white: #ffffff;
    --name-grey: #8c8386;
  }
  * { margin: 0; padding: 0; box-sizing: border-box; }
  html, body {
    width: 900px;
    height: 1200px;
    overflow: hidden;
    background: var(--panel-charcoal);
  }
  .sign {
    position: relative;
    width: 900px;
    height: 1200px;
    overflow: hidden;
    background: var(--panel-charcoal);
    font-family: "Open Sans", Arial, sans-serif;
    color: var(--sign-white);
  }
  .status-panel {
    position: absolute;
    inset: 0 0 auto 0;
    height: 282px;
    background: var(--header-black);
    display: flex;
    align-items: center;
    justify-content: center;
  }
  .status-panel h1 {
    font-weight: 700;
    font-size: 116px;
    letter-spacing: 1px;
    line-height: 1;
    margin-top: -6px;
    white-space: nowrap;
  }
  .brand {
    position: absolute;
    top: 430px;
    left: 0;
    width: 900px;
    display: flex;
    align-items: center;
    justify-content: center;
    gap: 28px;
  }
  .brand-square {
    width: 70px;
    height: 70px;
    background: var(--sign-white);
  }
  .brand-name {
    font-weight: 700;
    font-size: 84px;
    line-height: 1;
    letter-spacing: -1px;
    white-space: nowrap;
  }
  .agent-bar {
    position: absolute;
    top: 722px;
    left: 0;
    width: 755px;
    height: 116px;
    background: var(--sign-white);
    display: flex;
    align-items: center;
    padding-left: 62px;
  }
  .agent-name {
    color: var(--name-grey);
    font-weight: 400;
    font-size: 68px;
    line-height: 1;
    letter-spacing: 0;
    white-space: nowrap;
  }
  .contact-list {
    position: absolute;
    top: 880px;
    left: 50px;
    list-style: none;
  }
  .contact-list li {
    display: flex;
    align-items: center;
    height: 62px;
    font-size: 46px;
    font-weight: 400;
    letter-spacing: 0.3px;
    white-space: nowrap;
  }
  .contact-list svg {
    width: 52px;
    height: 52px;
    margin-right: 38px;
    flex: none;
  }
  .phone {
    position: absolute;
    top: 1025px;
    left: 0;
    width: 900px;
    text-align: center;
    font-size: 124px;
    font-weight: 400;
    line-height: 1.2;
    letter-spacing: 1px;
    white-space: nowrap;
  }
</style>
</head>
<body>
  <main class="sign">
    <header class="status-panel">
      <h1>FOR SALE</h1>
    </header>

    <div class="brand">
      <span class="brand-square" aria-hidden="true"></span>
      <span class="brand-name">BrightLane</span>
    </div>

    <div class="agent-bar">
      <p class="agent-name">DESMOND HARLOW</p>
    </div>

    <ul class="contact-list">
      <li>
        <svg viewBox="0 0 52 52" aria-hidden="true" fill="none" stroke="#fff" stroke-width="2.6">
          <circle cx="26" cy="26" r="20"/>
          <ellipse cx="26" cy="26" rx="9" ry="20"/>
          <line x1="6" y1="26" x2="46" y2="26"/>
          <path d="M10 15 H42 M10 37 H42"/>
        </svg>
        <span>www.blrealestate.com.au</span>
      </li>
      <li>
        <svg viewBox="0 0 52 52" aria-hidden="true" fill="none" stroke="#fff" stroke-width="2.6">
          <rect x="3" y="12" width="46" height="30" rx="2"/>
          <path d="M3 13 L26 30 L49 13"/>
        </svg>
        <span>sales@blrealestate.com.au</span>
      </li>
    </ul>

    <p class="phone">0491 836 205</p>
  </main>
</body>
</html>
```